Marwick Law Letterhead

We need a new letterhead design for a Law Firm. The address for the law firm is 4175 Calloway Avenue, Suite 200, Houston, Texas 77046. Phone Number: 832-614-2093; Fax Number: 832-307-1546. The logo is uploaded to the project.

```html
<!DOCTYPE html>
<html lang="en">
<head>
<meta charset="utf-8">
<title>Marwick Law Letterhead</title>
<link rel="stylesheet" href="https://fonts.googleapis.com/css2?family=Open+Sans:wght@400;600&family=Roboto:wght@400;500&display=swap">
<style>
  :root {
    --backdrop: #dcdcdc;
    --paper: #f7f7f7;
    --navy: #1c2b5a;
    --red: #e31b23;
    --ink: #444444;
    --ink-dark: #222222;
    --white: #ffffff;
  }
  * { margin: 0; padding: 0; box-sizing: border-box; }
  html, body {
    width: 1153px; height: 1200px; overflow: hidden;
    background: var(--backdrop);
  }
  .letterhead {
    position: absolute; left: 168px; top: 30px;
    width: 816px; height: 1139px;
    background: var(--paper);
    box-shadow: 0 10px 30px rgba(0,0,0,0.12);
    overflow: hidden;
  }
  .brand {
    position: absolute; left: 87px; top: 92px;
    display: flex; align-items: center; gap: 12px;
  }
  .brand-mark {
    width: 46px; height: 46px; border-radius: 50%;
    background: var(--navy);
  }
  .brand-name {
    font-family: "Open Sans", sans-serif; font-weight: 600;
    font-size: 30px; color: var(--navy); letter-spacing: 0.5px;
  }
  .contact {
    position: absolute; left: 539px; top: 63px;
    font-family: "Roboto", sans-serif; font-size: 13px;
    line-height: 16px; color: var(--ink-dark);
  }
  .contact-address { margin-bottom: 8px; }
  .contact-line { display: flex; align-items: center; gap: 5px; height: 17px; }
  .contact-line svg { width: 12px; height: 12px; flex: none; }
  .letter {
    position: absolute; left: 87px; top: 287px; width: 641px;
    font-family: "Open Sans", sans-serif; font-size: 14.6px;
    line-height: 21px; color: var(--ink);
  }
  .letter p { margin-bottom: 21px; text-align: justify; }
  .letter .salutation, .letter .closing { text-align: left; }
  .signature {
    position: absolute; left: 87px; top: 839px;
    width: 93px; height: 87px;
    background: linear-gradient(135deg, #e6e6e6, #d2d2d2);
  }
  .footer-band {
    position: absolute; left: 0; bottom: 0; width: 816px; height: 30px;
  }
  .footer-web {
    position: absolute; right: 0; bottom: 0; width: 264px; height: 30px;
    padding-left: 20px;
    display: flex; align-items: center; justify-content: center;
    font-family: "Roboto", sans-serif; font-weight: 500; font-size: 15px;
    color: var(--white);
  }
</style>
</head>
<body>
  <main class="letterhead">
    <header>
      <div class="brand">
        <span class="brand-mark"></span>
        <span class="brand-name">Marwick Law</span>
      </div>
      <address class="contact" style="font-style:normal">
        <div class="contact-address">4175 Calloway Avenue,<br>Suite 200, Houston,<br>Texas 77046.</div>
        <div class="contact-line">
          <svg viewBox="0 0 24 24"><path fill="var(--red)" d="M6.6 10.8a15.1 15.1 0 0 0 6.6 6.6l2.2-2.2c.3-.3.7-.4 1-.2 1.1.4 2.3.6 3.6.6.6 0 1 .4 1 1V20c0 .6-.4 1-1 1A17 17 0 0 1 3 4c0-.6.4-1 1-1h3.5c.6 0 1 .4 1 1 0 1.3.2 2.5.6 3.6.1.3 0 .7-.2 1z"/></svg>
          <span>832-614-2093</span>
        </div>
        <div class="contact-line">
          <svg viewBox="0 0 24 24"><path fill="var(--red)" d="M6 2h12v5H6zM3 8h18a1 1 0 0 1 1 1v8h-4v5H6v-5H2V9a1 1 0 0 1 1-1zm5 7v5h8v-5z"/></svg>
          <span>832-307-1546</span>
        </div>
        <div class="contact-line">
          <svg viewBox="0 0 24 24"><path fill="var(--red)" d="M2 5h20v14H2zm2 2v.5l8 5 8-5V7l-8 5z"/></svg>
          <span>contact@marwickinjury.com</span>
        </div>
      </address>
    </header>

    <article class="letter">
      <p class="salutation">Dear customer,</p>
      <p>Lorem ipsum dolor sit amet, consectetur adipisicing elit, sed do eiusmod tempor incididunt ut labore et dolore magna aliqua. Ut enim ad minim veniam, quis nostrud exercitation ullamco laboris nisi ut aliquip ex ea commodo consequat. Duis aute irure dolor in reprehenderit in voluptate velit esse cillum dolore eu fugiat nulla pariatur. Excepteur sint occaecat cupidatat non proident, sunt in culpa qui officia deserunt mollit anim id est laborum.</p>
      <p>Lorem ipsum dolor sit amet, consectetur adipisicing elit, sed do eiusmod tempor incididunt ut labore et dolore magna aliqua. Ut enim ad minim veniam, quis nostrud exercitation ullamco laboris nisi ut aliquip ex ea commodo consequat. Duis aute irure dolor in reprehenderit in voluptate velit esse cillum dolore eu fugiat nulla pariatur. Excepteur sint occaecat cupidatat non proident, sunt in culpa qui officia deserunt mollit anim id est laborum.</p>
      <p>Lorem ipsum dolor sit amet, consectetur adipisicing elit, sed do eiusmod tempor incididunt ut labore et dolore magna aliqua. Ut enim ad minim veniam, quis nostrud exercitation ullamco laboris nisi ut aliquip ex ea commodo consequat. Duis aute irure dolor in reprehenderit in voluptate velit esse cillum dolore eu fugiat nulla pariatur. Excepteur sint occaecat cupidatat non proident, sunt in culpa qui officia deserunt mollit anim id est laborum.</p>
      <p>Lorem ipsum dolor sit amet, consectetur adipisicing elit, sed do eiusmod tempor incididunt ut labore et dolore magna aliqua. Ut enim ad minim veniam, quis nostrud exercitation ullamco laboris nisi ut aliquip ex ea commodo consequat. Duis aute irure dolor in reprehenderit.</p>
      <p class="closing">Yours Sincerely,</p>
    </article>

    <div class="signature" role="img" aria-label="Handwritten signature"></div>

    <footer>
      <svg class="footer-band" viewBox="0 0 816 30" preserveAspectRatio="none">
        <polygon points="0,12 536,12 536,30 0,30" fill="var(--navy)"/>
        <polygon points="552,0 816,0 816,30 528,30" fill="var(--red)"/>
        <polygon points="536,12 543,12 528,30 521,30" fill="var(--paper)"/>
      </svg>
      <div class="footer-web">www.marwickinjury.com</div>
    </footer>
  </main>
</body>
</html>
```